OpenCart website

We have an existing site that was based on open cart in 2011 but customised heavily. We want a brand new open cart site designed from scratch so we can work on transitioning the existing opencart database over after the project is done

Current site: www.tallowfinchgoods.com

```html
<!DOCTYPE html>
<html lang="en">
<head>
<meta charset="utf-8">
<title>Tallowfinch Goods</title>
<link href="https://fonts.googleapis.com/css2?family=Source+Sans+3:wght@400;600;700&display=swap" rel="stylesheet">
<style>
:root{
  --red:#ee2a2a;
  --dark:#222222;
  --footer:#232323;
  --text:#333333;
  --muted:#666666;
  --line:#e4e4e4;
  --tile:#eef0f4;
  --cream:#faf2e0;
  --mint:#e0fbfb;
  --grey:#e1e1e1;
  --sky:#d3e8f8;
}
*{box-sizing:border-box;margin:0;padding:0}
html,body{width:1200px;height:3051px;overflow:hidden}
body{font-family:"Source Sans 3",sans-serif;color:var(--text);background:#fff;position:relative}
.abs{position:absolute}
a{color:inherit;text-decoration:none}

.topbar{left:0;top:0;width:1200px;height:36px;background:#f4f5f7;font-size:11px;color:#555}
.topbar .links{position:absolute;right:150px;top:11px;display:flex;gap:10px}
.header{left:0;top:36px;width:1200px;height:77px}
.logo{left:149px;top:14px;font-size:22px;font-weight:700;color:var(--red);display:flex;align-items:center;gap:8px}
.logo .mark{width:14px;height:14px;background:var(--red)}
.search{left:397px;top:21px;width:494px;height:34px;display:flex}
.search .field{flex:1;border:1px solid #ddd;font-size:10px;color:#888;padding:10px 13px}
.search .btn{width:90px;background:var(--red);color:#fff;font-size:12px;display:flex;align-items:center;justify-content:center}
.icon-user{left:956px;top:22px}
.icon-cart{left:1014px;top:20px}
.badge{left:1034px;top:18px;width:16px;height:16px;border-radius:50%;background:#111;color:#fff;font-size:9px;text-align:center;line-height:16px}
.nav{left:0;top:113px;width:1200px;height:39px;background:var(--dark);color:#fff;font-size:11px}
.nav span{position:absolute;top:14px}

.cats{left:149px;top:161px;width:190px;height:386px;border:1px solid var(--line)}
.cats .head{height:33px;background:var(--red);color:#fff;font-size:12px;display:flex;align-items:center;padding-left:18px;gap:10px}
.cats ul{list-style:none;margin-top:5px}
.cats li{height:23.3px;font-size:10px;padding-left:18px;line-height:23px}
.cats li:nth-child(even){background:#f2f3f5}
.hero{left:354px;top:161px;width:459px;height:386px;background:var(--cream)}
.hero .art{position:absolute;left:18px;top:40px;width:340px;height:140px;background:linear-gradient(90deg,#e2431f,#3ea857,#2f5fb8);border-radius:6px}
.hero h1{position:absolute;left:20px;top:222px;font-size:27px;font-weight:700;color:#222}
.hero p{position:absolute;left:22px;top:263px;font-size:12px;color:#555}
.outline-btn{position:absolute;left:24px;top:296px;border:1px solid var(--red);color:var(--red);font-size:11px;padding:5px 12px}
.promo{left:826px;width:224px;height:186px;background:var(--tile);border:1px solid var(--line)}
.promo h3{position:absolute;left:16px;top:22px;font-size:19px;font-weight:600;color:#222}
.promo .art{position:absolute;left:10px;bottom:8px;width:204px;height:80px;border-radius:6px}

.feature{top:603px;width:293px;height:103px;display:flex;align-items:center;padding-left:32px;gap:22px}
.feature .circ{width:42px;height:42px;border-radius:50%;background:rgba(0,0,0,.12);display:flex;align-items:center;justify-content:center}
.feature b{display:block;font-size:12px;font-weight:700;color:#222}
.feature small{font-size:9px;color:#555}

.section-title{left:0;width:1200px;top:790px;text-align:center;font-size:27px;font-weight:600;color:#333}
.rule{left:553px;top:830px;width:94px;height:2px;background:var(--red)}
.arrow{width:28px;height:27px;border:1px solid #ccc;display:flex;align-items:center;justify-content:center;background:#fff}
.card{top:872px;width:213px;height:345px;border:1px solid var(--line)}
.card .art{position:absolute;left:15px;top:14px;width:183px;height:220px;background:#eceef2}
.card .art i{position:absolute;left:14px;top:50px;width:155px;height:110px;border-radius:10px}
.card h4{position:absolute;left:17px;top:251px;font-size:13px;font-weight:600;color:#222}
.card p{position:absolute;left:17px;top:276px;font-size:11px;line-height:15px;color:#555}

.brands{left:149px;top:1332px;width:901px;height:76px;border-top:1px solid var(--line);border-bottom:1px solid var(--line)}
.brands .list{position:absolute;left:60px;right:60px;top:26px;display:flex;justify-content:space-between;font-size:15px;font-weight:600;color:#555}

.tile{width:285px;background:var(--tile)}
.tile h5{position:absolute;left:20px;top:36px;font-size:14px;font-weight:600;color:#222;letter-spacing:.2px}
.tile .art{position:absolute;left:20px;right:20px;top:70px;bottom:18px;border-radius:8px}
.photo{background:linear-gradient(160deg,#6f7a72,#4b4842 55%,#6b3b44)}
.photo .txt{position:absolute;left:0;width:285px;top:178px;text-align:center;color:#fff}
.photo .txt b{display:block;font-size:42px;font-weight:700;line-height:44px}
.photo .txt span{display:block;font-size:26px;font-weight:700}
.photo .go{display:inline-block;margin-top:10px;background:var(--red);color:#fff;font-size:11px;padding:5px 13px}
.quote{text-align:center}
.quote p{position:absolute;left:18px;right:18px;top:68px;font-size:10.5px;line-height:23px;color:#555}
.quote .avatar{position:absolute;left:84px;top:188px;width:116px;height:116px;border-radius:50%;border:4px solid #fff;background:linear-gradient(#3b3a40,#8a6b58)}
.quote b{position:absolute;left:0;width:285px;top:322px;font-size:13px;color:#222}
.quote small{position:absolute;left:0;width:285px;top:343px;font-size:10px;color:#444}

.footer{left:0;top:2599px;width:1200px;height:452px;background:var(--footer);color:#aaa}
.fcol{position:absolute;top:92px}
.fcol h6{font-size:12px;font-weight:700;color:#fff;margin-bottom:12px}
.fcol li{list-style:none;font-size:9.5px;height:27px}
.pay{position:absolute;top:99px;left:817px;width:232px;display:flex;justify-content:space-between;font-size:12px;font-weight:700;color:#888}
.subscribe{position:absolute;left:787px;top:139px;width:267px;height:40px;display:flex}
.subscribe .field{flex:1;background:#fff;color:#888;font-size:10px;padding:13px 13px}
.subscribe .btn{width:84px;background:var(--red);color:#fff;font-size:11px;display:flex;align-items:center;justify-content:center}
.social{position:absolute;top:203px;width:37px;height:37px;background:#fff;color:#222;font-size:9px;font-weight:700;display:flex;align-items:center;justify-content:center}
</style>
</head>
<body>

<div class="abs topbar"><div class="links"><span>Become a New Customer</span><span>|</span><span>Credit Application &amp; Prepaid Shipping</span><span>|</span><span>Download Credit Application</span></div></div>

<header class="abs header">
  <div class="abs logo"><span class="mark"></span>Tallowfinch Goods</div>
  <div class="abs search"><div class="field">Search Over 4,000 Products....</div><div class="btn">SEARCH</div></div>
  <svg class="abs icon-user" width="30" height="30" viewBox="0 0 30 30" fill="none" stroke="#777" stroke-width="1.6"><circle cx="15" cy="15" r="13.5"/><circle cx="15" cy="11" r="5"/><path d="M6 24c2-5 16-5 18 0"/></svg>
  <svg class="abs icon-cart" width="26" height="30" viewBox="0 0 26 30" fill="none" stroke="#333" stroke-width="1.8"><rect x="3" y="9" width="20" height="19" rx="3"/><path d="M8 12V7a5 5 0 0 1 10 0v5"/></svg>
  <div class="abs badge">0</div>
</header>

<nav class="abs nav">
  <span style="left:149px">HOME</span><span style="left:216px">ABOUT US</span><span style="left:303px">MY ACCOUNT</span><span style="left:404px">MY SHOPPING LIST</span><span style="left:532px">LOCATION &amp; CONTACTS</span><span style="left:682px">SITE MAP</span>
</nav>

<aside class="abs cats">
  <div class="head"><svg width="12" height="10"><path d="M0 1h12M0 5h12M0 9h12" stroke="#fff" stroke-width="1.6"/></svg>ALL CATEGORIES</div>
  <ul>
    <li>Cleaning Supplies</li><li>Cookware And Baking</li><li>Crafts And Hobbies</li><li>Food</li><li>Glassware</li><li>Hardware</li><li>Health And Beauty</li><li>Home Accesories</li><li>Kitchenware</li><li>Plasticware</li><li>Seasonal</li><li>Stainless Steel</li><li>Tableware</li><li>Opportunity Buys</li>
  </ul>
</aside>

<section class="abs hero">
  <div class="art" role="img" aria-label="Red baking dish and set of coloured square food containers"></div>
  <h1>FOOD CONTAINERS</h1>
  <p>Vivamus id dolor nunc. Vivamus vehicula nisl elementum sollicitudin finibus.</p>
  <a class="outline-btn">Learn More</a>
</section>

<div class="abs promo" style="top:161px">
  <h3>SALE<br><span style="color:var(--red);font-size:17px;margin-left:52px">20% OFF</span></h3>
  <div class="art" role="img" aria-label="Blue enamel camping cookware set" style="background:linear-gradient(90deg,#2c3f86,#4f66b4,#9aa4b8)"></div>
</div>
<div class="abs promo" style="top:361px;background:#fff">
  <h3 style="font-size:17px">NEW <span style="color:var(--red)">ARRIVALS</span></h3>
  <div class="art" role="img" aria-label="Amber glass skull decanter and shot glass gift set" style="background:linear-gradient(90deg,#d99a2a,#f0c25a,#e8e2d6)"></div>
</div>

<div class="abs feature" style="left:149px;background:var(--mint)">
  <div class="circ"><svg width="24" height="16" fill="none" stroke="#333" stroke-width="1.3"><rect x="1" y="2" width="14" height="10"/><path d="M15 5h5l3 4v3h-8"/><circle cx="5" cy="13" r="2" fill="#fff"/><circle cx="19" cy="13" r="2" fill="#fff"/></svg></div>
  <div><b>FREE SHIPPING</b><small>On orders over &nbsp;$ 99</small></div>
</div>
<div class="abs feature" style="left:454px;background:var(--grey)">
  <div class="circ"><svg width="20" height="20" fill="none" stroke="#222" stroke-width="2"><path d="M5 6a7 7 0 1 0 5-2"/><path d="M10 1v6H4" /></svg></div>
  <div><b>ORDER RETURN</b><small>Returns within 7 days</small></div>
</div>
<div class="abs feature" style="left:757px;background:var(--sky)">
  <div class="circ"><svg width="22" height="16" fill="none" stroke="#333" stroke-width="1.3"><rect x="1" y="1" width="20" height="14"/><path d="M1 1l10 8 10-8"/></svg></div>
  <div><b>CONTACT US</b><small>Contact us for support services</small></div>
</div>

<h2 class="abs section-title">New Arrivals</h2>
<div class="abs rule"></div>
<div class="abs arrow" style="left:977px;top:820px"><svg width="8" height="10"><path d="M6 1L2 5l4 4" stroke="#333" fill="none" stroke-width="1.5"/></svg></div>
<div class="abs arrow" style="left:1021px;top:820px"><svg width="8" height="10"><path d="M2 1l4 4-4 4" stroke="#333" fill="none" stroke-width="1.5"/></svg></div>

<div class="abs card" style="left:149px"><div class="art"><i role="img" aria-label="Four white sport bottles with coloured grips" style="background:linear-gradient(90deg,#e94b3c,#3aa54b,#e2447c,#3c4fae)"></i></div><h4>Bottle Sport Soft Grip 22oz</h4><p>Item No: 072517<br>Inner Pack: 0<br>Case Pack: 36</p></div>
<div class="abs card" style="left:378px"><div class="art"><i role="img" aria-label="Burgundy and blue travel mugs" style="background:linear-gradient(90deg,#6d2040,#1d3f9c)"></i></div><h4>Bottle Sport Soft Grip 22oz</h4><p>Item No: 072517<br>Inner Pack: 0<br>Case Pack: 36</p></div>
<div class="abs card" style="left:607px"><div class="art"><i role="img" aria-label="Red and steel mixing bowl set with utensils" style="background:linear-gradient(90deg,#c9ccd3,#d93b3b,#b8bcc4)"></i></div><h4>Bottle Sport Soft Grip 22oz</h4><p>Item No: 072517<br>Inner Pack: 0<br>Case Pack: 36</p></div>
<div class="abs card" style="left:837px"><div class="art"><i role="img" aria-label="Red and green kitchen timers in packaging" style="background:linear-gradient(90deg,#d9362f,#e9e2c8,#7cc23c)"></i></div><h4>Bottle Sport Soft Grip 22oz</h4><p>Item No: 072517<br>Inner Pack: 0<br>Case Pack: 36</p></div>

<div class="abs brands">
  <div class="abs arrow" style="left:0;top:24px"><svg width="8" height="10"><path d="M6 1L2 5l4 4" stroke="#333" fill="none" stroke-width="1.5"/></svg></div>
  <div class="list"><span>Brightly</span><span>Lumen Care</span><span>Veloro</span><span>Greenleaf</span><span>Marlow</span><span>Tessane</span><span>Emberline</span></div>
  <div class="abs arrow" style="right:0;top:24px"><svg width="8" height="10"><path d="M2 1l4 4-4 4" stroke="#333" fill="none" stroke-width="1.5"/></svg></div>
</div>

<div class="abs tile photo" style="left:149px;top:1488px;height:430px" role="img" aria-label="Glass jar of white beans on a striped cloth">
  <div class="txt"><b>SALE</b><span>20% OFF</span><a class="go">Learn More</a></div>
</div>
<div class="abs tile" style="left:149px;top:1943px;height:284px"><h5>SUSPENDISSE ACCUMSAN</h5><div class="art" role="img" aria-label="Four patterned ceramic bowls" style="background:linear-gradient(135deg,#c8644c,#2f2f2f,#2b3a7a)"></div></div>
<div class="abs tile" style="left:149px;top:2251px;height:284px"><h5>SUSPENDISSE ACCUMSAN</h5><div class="art" role="img" aria-label="Colourful toy watering cans" style="background:linear-gradient(135deg,#2f7fd6,#3ab54a,#e5e23a,#e94c9a)"></div></div>

<div class="abs tile" style="left:457px;top:1488px;height:284px"><h5>SUSPENDISSE ACCUMSAN</h5><div class="art" role="img" aria-label="Coloured glass mason jar mugs" style="background:linear-gradient(90deg,#38a8d6,#6cc22c,#8a52c8,#b0302a)"></div></div>
<div class="abs tile quote" style="left:457px;top:1796px;height:430px">
  <p>"Quisque egestas pharetra sagittis. Class aptent sociosqu ad litora torquent per conubia nostri inceptos himenaeos. Donec convallis sit amet purus sed ullamcorper. Suspendisse accumsan rutrum justo aliquam accumsan."</p>
  <div class="avatar" role="img" aria-label="Customer portrait"></div>
  <b>Maren Holloway</b><small>Montreal</small>
</div>
<div class="abs tile" style="left:457px;top:2251px;height:284px"><h5>SUSPENDISSE ACCUMSAN</h5><div class="art" role="img" aria-label="Blue mop bucket with white wringer" style="background:linear-gradient(135deg,#f2f2f2,#1e4fd0)"></div></div>

<div class="abs tile" style="left:765px;top:1488px;height:284px"><h5>SUSPENDISSE ACCUMSAN</h5><div class="art" role="img" aria-label="Collapsible coloured measuring cups with spices" style="background:linear-gradient(135deg,#b5562a,#2fa8d8,#e4322f,#3a3a3a)"></div></div>
<div class="abs tile" style="left:765px;top:1795px;height:284px"><h5>SUSPENDISSE ACCUMSAN</h5><div class="art" role="img" aria-label="Cast iron frying pans" style="background:linear-gradient(135deg,#1f1f1f,#6b5a4c,#2a2a2a)"></div></div>
<div class="abs tile" style="left:765px;top:2105px;height:430px"><h5 style="top:44px">SUSPENDISSE ACCUMSAN</h5><div class="art" role="img" aria-label="Navy and red electric pepper mills with box" style="top:110px;background:linear-gradient(90deg,#1b2240,#d1262c,#e8e0dc)"></div></div>

<footer class="abs footer">
  <ul class="fcol" style="left:158px"><h6>HELP</h6><li>Support Center</li><li>Contact Us</li><li>Return Policy</li><li>Shipping</li><li>Payment Options</li><li>Discounts</li><li>100% Guarantee</li><li>References</li><li>Buyer Guide</li><li>Sitemap</li></ul>
  <ul class="fcol" style="left:300px"><h6>MY ACCOUNT</h6><li>Login / Register</li><li>Track My Order</li><li>T&amp;C</li><li>Privacy</li></ul>
  <ul class="fcol" style="left:464px"><h6>COMPANY INFO</h6><li>About Us</li><li>Why Buy From Us</li><li>FAQ</li><li>Blog</li><li>Winners</li></ul>
  <ul class="fcol" style="left:629px"><h6>PARTNET PROGRAM</h6><li>Affiliates</li></ul>
  <div class="pay"><span>Payvia</span><span>Crestcard</span><span>Meridian</span></div>
  <div class="subscribe"><div class="field">E-mail Address</div><div class="btn">SUBSCRIBE</div></div>
  <div class="social" style="left:868px">Chirp</div>
  <div class="social" style="left:917px">Folio</div>
  <div class="social" style="left:966px">Pinlo</div>
  <div class="social" style="left:1014px">Gloop</div>
</footer>

</body>
</html>
```